Business card design for crowd sourced review site.

I need a business card magnet design for an online, crowd-sourced, restaurant review site strictly for Kosher restaurants.
It is similar to RoamLedger but catering to a very particular crowd.
The markets it will be distributed in are flooded with business card fridge magnets so this needs to be eye-catching and unique. The Business name is PlateMarks
The website isnt finished but you can see the basic setup here
http://restaurant.vintrello.com/

The second image i included is another logo design I liked and was thinking about using and decided I will probably also make a SECOND custom cut business card in the shape of that icon. Bonus if you can throw that in also.

Target Market(s)

Jewish consumers aged 20-35

Industry/Entity Type

Business

Contact Information for Business Card

see description.
Design should not be too crowded and should in eye-catching. Will mainly be used as fridge magnets.

Requirements
Must have
• Website address. logo.
Nice to have
• tagline. (The Definitive guide to kosher dining for the Kosher consumer)
• Im not a professional but I personally think the color blue goes along with this concept. ill leave it to you to decide.
Should not have
• any religious symbols.

```html
<!DOCTYPE html>
<html lang="en">
<head>
<meta charset="utf-8">
<title>PlateMarks Business Card</title>
<link rel="stylesheet" href="https://fonts.googleapis.com/css2?family=Open+Sans:wght@400;600;700&display=swap">
<style>
  :root {
    --page-bg: #e9e7e3;
    --card-bg: #f7f7f5;
    --card-shade: #e6e6e3;
    --accent: #e8693a;
    --accent-soft: #f0a07a;
    --ink: #2b2b2b;
    --muted: #555555;
  }
  * { box-sizing: border-box; margin: 0; padding: 0; }
  html, body {
    width: 1200px;
    height: 780px;
    overflow: hidden;
    background: var(--page-bg);
    font-family: "Open Sans", Arial, sans-serif;
  }
  .stage {
    width: 1200px;
    height: 780px;
    display: flex;
    align-items: center;
    justify-content: center;
  }
  .card {
    position: relative;
    width: 900px;
    height: 515px;
    background: var(--card-bg);
    border-radius: 4px;
    box-shadow: 0 6px 24px rgba(0,0,0,0.12);
    overflow: hidden;
  }
  .card-texture {
    position: absolute;
    inset: 0;
    background: radial-gradient(ellipse at 45% 40%, #ffffff 0%, var(--card-bg) 45%, var(--card-shade) 100%);
  }
  .brand {
    position: absolute;
    left: 70px;
    top: 70px;
    display: flex;
    align-items: center;
    gap: 16px;
  }
  .brand-dot {
    width: 46px;
    height: 46px;
    border-radius: 50%;
    background: var(--accent);
  }
  .brand-name {
    font-size: 58px;
    font-weight: 700;
    color: var(--accent);
    letter-spacing: 0.5px;
    line-height: 1;
  }
  .tagline {
    position: absolute;
    left: 70px;
    top: 158px;
    font-size: 27px;
    color: var(--ink);
    letter-spacing: 0.3px;
  }
  .person {
    position: absolute;
    left: 118px;
    top: 250px;
  }
  .person-name {
    font-size: 30px;
    font-weight: 700;
    color: var(--accent);
    letter-spacing: 1px;
    line-height: 1.1;
  }
  .person-role {
    font-size: 24px;
    color: var(--muted);
  }
  .contacts {
    position: absolute;
    left: 118px;
    top: 350px;
    list-style: none;
    font-size: 24px;
    color: var(--ink);
    line-height: 1.4;
  }
  .contacts .label {
    color: var(--accent-soft);
    margin-right: 6px;
  }
  .website {
    position: absolute;
    right: 60px;
    bottom: 60px;
    font-size: 24px;
    color: var(--ink);
    letter-spacing: 0.3px;
  }
</style>
</head>
<body>
  <main class="stage">
    <section class="card" aria-label="PlateMarks business card">
      <div class="card-texture" role="img" aria-label="Faint pale grey food illustration pattern across the card background"></div>

      <div class="brand">
        <span class="brand-dot"></span>
        <span class="brand-name">PlateMarks</span>
      </div>

      <p class="tagline">The Definitive guide to kosher dining for the Kosher consumer</p>

      <div class="person">
        <p class="person-name">JHON SMITH</p>
        <p class="person-role">Director</p>
      </div>

      <ul class="contacts">
        <li><span class="label">P:</span>(01) 2345 6789</li>
        <li><span class="label">F:</span>(01) 2345 6789</li>
        <li><span class="label">E:</span>Info@yourcompany.com</li>
      </ul>

      <p class="website">http://restaurant.vintrello.com/</p>
    </section>
  </main>
</body>
</html>
```